Step Boldly Toward Gain Promotional Flyer

I Need a one page, one-sided 8.5 x 11 editable promotional flyer that POPS!, designed in photoshop

[TITLE]Step Boldly Toward Gain: 3 BOLD Moves to Up-Level Your Business Now!

[CONTENT for the Flyer:]

At this content-rich event you will learn how to:
• Get out of feast and famine mode and into six, multi-six and/or seven figure-income mode
• Leapfrog your competition and become the obvious choice in your market
• Have your business aligned with who you are and what you want
• Enjoy your business far more than you imagined possible.
• Have more fun and time to yourself
• Live free and unbound!

Accolades
“Delphine helped us increase our six figure income by 41%...I feel reborn!” Marlene & Otis Pruitt, Vienna, VA

“…Delphine is a joy to listen to - compelling, smart, provocative…” – Dennis Ashcombe, Charlotte, North Carolina

“Delphine helped me increase my business by 66%...without me spending more time, money, or making cold calls! …I am in the zone!” Tina Worsley, Baltimore, MD
“Delphine is an energetic and dynamic speaker…content-rich…holds your attention to the very end!” Neil Barrow, Frmr Pres., Crane & Whitby, MD, MD, D.C., PA, DE, NJ
“Delphine is the real estate whisperer!” Hal Drummond, Washington D.C.

“Delphine was prepared, funny, informative and made a connection with each of our agents…Fabulous!…even my admins were PUMPED!!! – Paul Venable, New York

About Delphine:
Delphine is a highly regarded business development speaker & coach who knows how to pump up an audience and have them making more money, in less time, AND having more fun doing it! What’s not to love?! Consistently rated as an exceptional speaker and conference favorite! Among her work: Standout Method: How to Draw Your Best Buyers Time after Time!, Contact Sourcing Done Easy, The Worst Outreach Errors Real Estate Agents Commit and How to Steer Clear of Them, Slow Seasons Build Sharp Sellers, Drive Within the Head for Real Estate Agents.

[Also need a section for:]
Date: December 9, 2015, Time: 9:00 Am - 12:00 Noon, Place: Harbor Lantern Convention, Green Castle, PA

Target Market(s)

Real Estate Agents

Industry/Entity Type

Real Estate Agent

Font styles to use
Sans Serif

Colors
0655a3
f37122

Requirements
Must have
• the peak tier realty mentor logo
Nice to have
• step boldly toward gain logo; lots of POP! :-) ; open to other colors, accent colors.

```html
<!DOCTYPE html>
<html lang="en">
<head>
<meta charset="utf-8">
<title>Step Boldly Toward Gain – Event Flyer</title>
<link rel="stylesheet" href="https://fonts.googleapis.com/css2?family=Arimo:ital,wght@0,400;0,700;1,400&display=swap">
<style>
:root{
  --navy:#0b2253;
  --blue:#0655a3;
  --orange:#f37122;
  --grey-panel:#e6e6e6;
  --text:#3c3c3c;
  --white:#ffffff;
}
*{box-sizing:border-box;margin:0;padding:0}
html,body{width:932px;height:1200px;overflow:hidden;background:var(--white)}
body{font-family:"Arimo",Arial,sans-serif;color:var(--text)}
.flyer{position:relative;width:932px;height:1200px;background:var(--white);border:12px solid var(--navy);overflow:hidden}
.flyer > *{position:absolute}
.decor{left:-12px;top:-12px;width:932px;height:1200px}

.brand-mark{right:38px;top:28px;display:flex;align-items:center;gap:10px;color:var(--white);font-size:30px;font-weight:400}
.brand-mark .dot{width:14px;height:14px;border-radius:50%;background:var(--orange)}

.speaker-photo{left:20px;top:118px;width:401px;height:172px;background:linear-gradient(90deg,#e9e9ea 0%,#d7d3cf 55%,#b9aea4 100%)}
.mentor-mark{left:40px;top:160px;width:240px;color:var(--orange);font-weight:700;font-size:30px;line-height:1.05}
.tagline{left:20px;top:290px;width:401px;height:30px;background:var(--orange);color:var(--white);font-style:italic;font-size:13.5px;text-align:center;line-height:30px}

.about{left:20px;top:320px;width:401px;height:345px;background:var(--blue);color:var(--white);padding:10px 18px 0 12px}
.about h2{font-size:21px;font-weight:700;margin-bottom:5px}
.about p{font-size:15.4px;line-height:24.8px;text-align:justify}

.learn{left:425px;top:118px;width:486px;height:547px;background:var(--grey-panel);padding:40px 20px 0 22px}
.learn h1{color:var(--orange);font-size:31px;line-height:36px;font-weight:700}
.learn h1 span{display:block;color:var(--blue);font-size:28px;line-height:38px}
.learn h3{color:var(--blue);font-size:19px;font-weight:700;margin:14px 0 12px -4px}
.learn ul{list-style:none}
.learn li{position:relative;padding-left:36px;font-size:16.5px;line-height:20px;color:#555;margin-bottom:15px}
.learn li svg{position:absolute;left:0;top:3px;width:20px;height:18px}

.accolades-title{left:20px;top:682px;width:869px;border-bottom:1px solid #555;color:var(--orange);font-size:24px;font-weight:700;padding-bottom:4px}
.quotes{top:732px}
.quotes.left{left:20px;width:380px}
.quotes.right{left:432px;width:460px}
.quote{font-size:16.5px;line-height:24px;color:var(--text);margin-bottom:22px}
.quote cite{display:block;font-style:normal;color:var(--blue)}

.event-info{left:246px;top:1116px;font-size:16.5px;font-weight:700;color:var(--white);line-height:25px}
.divider{left:477px;top:1112px;width:1px;height:58px;background:var(--white)}
.place{left:492px;top:1131px;font-size:15px;font-weight:700;color:var(--white);white-space:nowrap}
</style>
</head>
<body>
<div class="flyer">
  <svg class="decor" viewBox="0 0 932 1200" aria-hidden="true">
    <path d="M0 0H932V146C700 112 330 30 0 18Z" fill="var(--navy)"/>
    <path d="M70 24C360 34 700 108 932 152" fill="none" stroke="var(--orange)" stroke-width="5"/>
    <path d="M0 1128C300 1072 650 1062 932 1092V1200H0Z" fill="var(--orange)"/>
    <path d="M0 1122C300 1066 650 1056 932 1086" fill="none" stroke="var(--navy)" stroke-width="5"/>
  </svg>

  <div class="brand-mark"><span class="dot"></span>Step Boldly Toward Gain</div>

  <div class="speaker-photo" role="img" aria-label="Portrait photograph of speaker Delphine Marsh"></div>
  <div class="mentor-mark">Peak Tier Realty Mentor</div>
  <div class="tagline">“America’s Peak Tier Realty Mentor”™</div>

  <section class="about">
    <h2>About Delphine</h2>
    <p>Delphine is a highly regarded business development speaker &amp; coach who knows how to pump up an audience and have them making more money, in less time, AND having more fun doing it! What’s not to love?! Consistently rated as an exceptional speaker and conference favorite! Among her work: Standout Method: How to Draw Your Best Buyers Time after Time!, Contact Sourcing Done Easy, The Worst Outreach Errors Real Estate Agents Commit and How to Steer Clear of Them, Slow Seasons Build Sharp Sellers, Drive Within the Head for Real Estate Agents.</p>
  </section>

  <section class="learn">
    <h1>Step Boldly Toward Gain:<span>3 BOLD Moves to Up-Level Your Business Now!</span></h1>
    <h3>At this content-rich event you will learn how to:</h3>
    <ul>
      <li><svg viewBox="0 0 20 18"><path d="M2 10l5 5L18 2" fill="none" stroke="#666" stroke-width="3"/></svg>Get out of feast and famine mode and into six, multi-six and/or seven figure-income mode</li>
      <li><svg viewBox="0 0 20 18"><path d="M2 10l5 5L18 2" fill="none" stroke="#666" stroke-width="3"/></svg>Leapfrog your competition and become the obvious choice in your market</li>
      <li><svg viewBox="0 0 20 18"><path d="M2 10l5 5L18 2" fill="none" stroke="#666" stroke-width="3"/></svg>Have your business aligned with who you are and what you want</li>
      <li><svg viewBox="0 0 20 18"><path d="M2 10l5 5L18 2" fill="none" stroke="#666" stroke-width="3"/></svg>Enjoy your business far more than you imagined possible.</li>
      <li><svg viewBox="0 0 20 18"><path d="M2 10l5 5L18 2" fill="none" stroke="#666" stroke-width="3"/></svg>Have more fun and time to yourself</li>
      <li><svg viewBox="0 0 20 18"><path d="M2 10l5 5L18 2" fill="none" stroke="#666" stroke-width="3"/></svg>Live free and unbound!</li>
    </ul>
  </section>

  <h2 class="accolades-title">Accolades</h2>
  <div class="quotes left">
    <p class="quote">“Delphine helped us increase our six figure income by 41%...I feel reborn!”<cite>Marlene &amp; Otis Pruitt, Vienna, VA</cite></p>
    <p class="quote">“…Delphine is a joy to listen to - compelling, smart, provocative…”<cite>– Dennis Ashcombe, Charlotte, North Carolina</cite></p>
    <p class="quote">“Delphine helped me increase my business by 66%...without me spending more time, money, or making cold calls! …I am in the zone!”<cite>Tina Worsley, Baltimore, MD</cite></p>
  </div>
  <div class="quotes right">
    <p class="quote">“Delphine is an energetic and dynamic speaker… content-rich… holds your attention to the very end!”<cite>Neil Barrow, Frmr Pres., Crane &amp; Whitby,<br>MD, MD, D.C., PA, DE, NJ</cite></p>
    <p class="quote">“Delphine is the real estate whisperer!”<cite>Hal Drummond, Washington D.C.</cite></p>
    <p class="quote">“Delphine was prepared, funny, informative and made a connection with each of our agents…Fabulous!…even my admins were PUMPED!!!<cite>– Paul Venable, New York</cite></p>
  </div>

  <div class="event-info">Date: December 9, 2015<br>Time: 9:00 Am - 12:00 Noon</div>
  <div class="divider"></div>
  <div class="place">Place: Harbor Lantern Convention, Green Castle, PA</div>
</div>
</body>
</html>
```